BRCW Business Cards

Business Cards should contain:
Bright Ridgeway Coating Works
Colin Pardew
M: 0418 675 913
E: brightRCW@tealmail.example
BRCW logo
TCG logo
Painting & Decorating
Licence # 671392K
slogan: see the finish of true craftsmanship

Target Market(s)

all aspect of painting

Industry/Entity Type

Trade

Contact Information for Business Card

Colin Pardew
M: 0418 675 913
E: brightRCW@tealmail.example
BRCW logo
TCG logo
Painting & Decorating
Licence # 671392K

Font styles to use
Serif
Sans Serif

Requirements
Must have
• clear design with nice backround
• two sides
• smal TCG logo
Nice to have
• easy to read
Should not have
• mess
• black
• plastics form

```html
<!DOCTYPE html>
<html lang="en">
<head>
<meta charset="utf-8">
<title>BRCW Business Cards</title>
<link rel="stylesheet" href="https://fonts.googleapis.com/css2?family=Lora:wght@400&family=Mulish:wght@300;400&display=swap">
<style>
  :root {
    --bg: #ebebeb;
    --card: #ffffff;
    --teal: #1d5447;
    --ink: #3a3a3a;
    --muted: #8a8a8a;
    --accent: #f15a24;
    --mark-tint-a: #eef0ec;
    --mark-tint-b: #f6ece6;
    --badge: #2f56a6;
  }
  * { margin: 0; padding: 0; box-sizing: border-box; }
  html, body { width: 1200px; height: 800px; overflow: hidden; background: var(--bg); }
  .canvas { position: relative; width: 1200px; height: 800px; }

  .card {
    position: absolute;
    width: 540px;
    height: 330px;
    background: var(--card);
    box-shadow: 0 2px 6px rgba(0,0,0,0.08);
    overflow: hidden;
  }
  .card--front { left: 50px; top: 60px; }
  .card--back { left: 610px; top: 410px; }

  .faint-mark {
    position: absolute;
    width: 190px;
    height: 220px;
    border-radius: 90px 90px 24px 24px;
    background: linear-gradient(160deg, var(--mark-tint-b), var(--mark-tint-a) 60%, #f3f3f1);
  }
  .card--front .faint-mark { left: 40px; top: 40px; }
  .card--back .faint-mark { right: 70px; top: 18px; width: 150px; height: 180px; }

  .tagline-block {
    position: absolute;
    left: 110px;
    top: 120px;
    display: flex;
    flex-direction: column;
    align-items: flex-end;
    gap: 4px;
  }
  .slogan {
    font-family: "Lora", serif;
    font-size: 24px;
    line-height: 1.2;
    color: #222;
    white-space: nowrap;
  }
  .trade {
    font-family: "Mulish", sans-serif;
    font-weight: 300;
    font-size: 16px;
    color: var(--muted);
    white-space: nowrap;
  }

  .front-marks {
    position: absolute;
    right: 30px;
    bottom: 36px;
    display: flex;
    align-items: center;
    gap: 26px;
  }
  .partner-badge { width: 44px; height: 34px; }
  .brand-small {
    display: flex;
    align-items: center;
    gap: 8px;
    font-family: "Lora", serif;
    font-size: 22px;
    color: var(--teal);
  }
  .brand-dot { width: 14px; height: 14px; border-radius: 50%; background: var(--teal); }

  .brand-lockup {
    position: absolute;
    left: 46px;
    top: 140px;
    display: flex;
    align-items: center;
    gap: 14px;
    font-family: "Lora", serif;
    color: var(--teal);
    font-weight: 400;
  }
  .brand-lockup .brand-dot { width: 26px; height: 26px; }
  .brand-name { font-size: 44px; line-height: 1; letter-spacing: 1px; }
  .brand-full { font-size: 15px; line-height: 1.3; margin-top: 6px; }

  .contact {
    position: absolute;
    right: 40px;
    top: 132px;
    text-align: right;
    font-family: "Mulish", sans-serif;
  }
  .contact-name {
    font-weight: 300;
    font-size: 24px;
    letter-spacing: 1.5px;
    color: var(--accent);
    text-transform: uppercase;
    margin-bottom: 8px;
    padding-right: 26px;
    white-space: nowrap;
  }
  .contact-line {
    display: flex;
    justify-content: flex-end;
    align-items: center;
    gap: 10px;
    font-size: 15px;
    color: var(--ink);
    line-height: 1.7;
    white-space: nowrap;
  }
  .contact-line--muted { color: var(--muted); }
  .contact-line svg { width: 16px; height: 16px; flex: none; }
</style>
</head>
<body>
<main class="canvas">

  <section class="card card--front" aria-label="Business card, slogan side">
    <div class="faint-mark" role="img" aria-label="Faint brand mark decoration"></div>
    <div class="tagline-block">
      <p class="slogan">see the finish of true craftsmanship</p>
      <p class="trade">Painting &amp; Decorating</p>
    </div>
    <div class="front-marks">
      <svg class="partner-badge" viewBox="0 0 44 34" role="img" aria-label="TCG membership badge">
        <rect x="2" y="2" width="40" height="30" rx="4" fill="var(--badge)"/>
      </svg>
      <div class="brand-small"><span class="brand-dot"></span>BRCW</div>
    </div>
  </section>

  <section class="card card--back" aria-label="Business card, contact side">
    <div class="faint-mark" role="img" aria-label="Faint brand mark decoration"></div>
    <div class="brand-lockup">
      <span class="brand-dot"></span>
      <div>
        <div class="brand-name">BRCW</div>
        <div class="brand-full">Bright Ridgeway<br>Coating Works</div>
      </div>
    </div>
    <div class="contact">
      <p class="contact-name">Colin Pardew</p>
      <p class="contact-line">0418 675 913
        <svg viewBox="0 0 16 16" aria-hidden="true"><rect x="4" y="1.5" width="8" height="13" rx="1.5" fill="none" stroke="var(--accent)" stroke-width="1.4"/><line x1="7" y1="12" x2="9" y2="12" stroke="var(--accent)" stroke-width="1.4"/></svg>
      </p>
      <p class="contact-line">brightRCW@tealmail.example
        <svg viewBox="0 0 16 16" aria-hidden="true"><rect x="1.5" y="3.5" width="13" height="9" fill="none" stroke="var(--accent)" stroke-width="1.4"/><path d="M1.5 3.5 L8 9 L14.5 3.5" fill="none" stroke="var(--accent)" stroke-width="1.4"/></svg>
      </p>
      <p class="contact-line contact-line--muted">Licence # 671392K
        <svg viewBox="0 0 16 16" aria-hidden="true"><circle cx="8" cy="6" r="4" fill="none" stroke="var(--accent)" stroke-width="1.4"/><path d="M5.5 9.5 L4.5 15 L8 13 L11.5 15 L10.5 9.5" fill="none" stroke="var(--accent)" stroke-width="1.4"/></svg>
      </p>
    </div>
  </section>

</main>
</body>
</html>
```